Startup Careers Fair Bunting/Banner

We'd need a bunting/banner(portrait) for an upcoming careers fair that we are going to be exhibiting at. We build innovative retail store management solutions, primarily an Vexo POS/Point of Sale on the cloud. We would like to see designs that use our primary colours of orange, black and white.

The final design should communicate a fun, exciting and attractive company to work at.

```html
<!DOCTYPE html>
<html lang="en">
<head>
<meta charset="utf-8">
<title>Tillora Careers Banner</title>
<link rel="stylesheet" href="https://fonts.googleapis.com/css2?family=Roboto+Condensed:wght@400;700&family=Roboto:wght@900&display=swap">
<style>
  :root {
    --orange: #f7941d;
    --black: #000000;
    --white: #ffffff;
    --ink: #1a1a1a;
    --grey: #8c8c8c;
    --logo-ink: #474747;
  }
  html, body { margin: 0; padding: 0; overflow: hidden; }
  body { width: 1200px; height: 3600px; background: var(--black); position: relative; font-family: "Roboto Condensed", Arial, sans-serif; }
  .banner { position: absolute; inset: 0; overflow: hidden; }
  .frame {
    position: absolute; left: 86px; top: 144px; width: 1050px; height: 3600px;
    background: var(--orange); border-radius: 96px 96px 0 0;
  }
  .headline-box {
    position: absolute; left: 112px; top: 176px; width: 998px; height: 352px;
    background: var(--white); border-radius: 72px 72px 0 0;
  }
  .headline-some {
    position: absolute; left: 176px; top: 218px; margin: 0;
    font-family: "Roboto", Arial, sans-serif; font-weight: 900; font-size: 150px; line-height: 1;
    color: var(--orange); letter-spacing: 2px;
  }
  .headline-career {
    position: absolute; left: 176px; top: 384px; margin: 0;
    font-weight: 700; font-size: 100px; line-height: 1; color: var(--ink);
  }
  .calling-band {
    position: absolute; left: 112px; top: 528px; width: 998px; height: 202px;
    display: flex; align-items: center; justify-content: center;
    font-weight: 700; font-size: 84px; color: var(--white); margin: 0;
  }
  .hero-photo {
    position: absolute; left: 112px; top: 730px; width: 998px; height: 1510px;
    background: radial-gradient(ellipse at 60% 35%, #4a4a4a 0%, #262626 35%, #0b0b0b 70%, #000 100%);
  }
  .content-panel { position: absolute; left: 112px; top: 2240px; width: 998px; height: 976px; background: var(--black); }
  .hiring-title {
    position: absolute; left: 0; right: 0; top: 2246px; margin: 0; text-align: center;
    font-weight: 700; font-size: 104px; color: var(--orange); line-height: 1;
  }
  .dotted-rule { position: absolute; left: 218px; width: 764px; border-top: 6px dotted var(--white); }
  .dotted-rule.top { top: 2366px; }
  .dotted-rule.bottom { top: 2790px; }
  .role-list { position: absolute; left: 180px; top: 2410px; margin: 0; padding: 0; list-style: none; }
  .role-list li {
    display: flex; align-items: center; height: 126px;
    font-size: 70px; color: var(--white); line-height: 1;
  }
  .role-list svg { width: 56px; height: 46px; margin-right: 36px; flex: none; }
  .feature-icons { position: absolute; left: 0; top: 2900px; width: 1200px; height: 240px; }
  .logo-strip {
    position: absolute; left: 112px; top: 3216px; width: 998px; height: 384px; background: var(--white);
    display: flex; align-items: center; justify-content: center; gap: 34px;
  }
  .logo-mark { width: 110px; height: 110px; background: var(--orange); }
  .logo-name { font-weight: 700; font-size: 140px; color: var(--logo-ink); line-height: 1; }
  .pointer { position: absolute; left: 0; top: 0; width: 1200px; height: 400px; }
</style>
</head>
<body>
<main class="banner">
  <div class="frame"></div>

  <div class="headline-box"></div>
  <h1 class="headline-some">SOME</h1>
  <p class="headline-career">CALL IT A CAREER</p>
  <p class="calling-band">FOR US, IT’S A CALLING</p>

  <div class="hero-photo" role="img" aria-label="Photo of a masked ninja in black holding a sword against a dark background"></div>

  <div class="content-panel"></div>
  <h2 class="hiring-title">NOW HIRING</h2>
  <div class="dotted-rule top"></div>
  <ul class="role-list">
    <li><svg viewBox="0 0 56 46"><path d="M0 15h30V0l26 23-26 23V31H0z" fill="#f7941d"/></svg>Customer Service Champions</li>
    <li><svg viewBox="0 0 56 46"><path d="M0 15h30V0l26 23-26 23V31H0z" fill="#f7941d"/></svg>Sales Warriors</li>
    <li><svg viewBox="0 0 56 46"><path d="M0 15h30V0l26 23-26 23V31H0z" fill="#f7941d"/></svg>Online Marketing Ninjas</li>
  </ul>
  <div class="dotted-rule bottom"></div>

  <svg class="feature-icons" viewBox="0 0 1200 240" aria-label="Cloud, cash register and tablet icons">
    <g fill="#8c8c8c">
      <!-- cloud -->
      <path d="M260 190h180a40 40 0 0 0 0-80 60 60 0 0 0-110-20 48 48 0 0 0-70 40 30 30 0 0 0 0 60z"/>
      <!-- cash register -->
      <rect x="600" y="30" width="70" height="40" rx="4"/>
      <rect x="628" y="70" width="14" height="30"/>
      <rect x="560" y="95" width="160" height="110" rx="8"/>
      <rect x="555" y="205" width="170" height="28" rx="4"/>
      <g fill="#000">
        <rect x="580" y="112" width="68" height="26"/>
        <rect x="664" y="112" width="38" height="18"/>
        <rect x="580" y="150" width="14" height="10"/><rect x="602" y="150" width="14" height="10"/><rect x="624" y="150" width="14" height="10"/>
        <rect x="580" y="168" width="14" height="10"/><rect x="602" y="168" width="14" height="10"/><rect x="624" y="168" width="14" height="10"/>
        <rect x="580" y="186" width="14" height="10"/><rect x="602" y="186" width="14" height="10"/><rect x="624" y="186" width="14" height="10"/>
        <rect x="664" y="150" width="38" height="46"/>
      </g>
      <!-- tablet -->
      <rect x="826" y="22" width="122" height="212" rx="16"/>
      <rect x="840" y="50" width="94" height="150" fill="#000"/>
      <rect x="870" y="34" width="34" height="6" rx="3" fill="#000"/>
      <circle cx="887" cy="216" r="8" fill="#000"/>
    </g>
  </svg>

  <div class="logo-strip">
    <span class="logo-mark"></span>
    <span class="logo-name">Tillora</span>
  </div>

  <svg class="pointer" viewBox="0 0 1200 400" aria-hidden="true">
    <g fill="#f7941d" stroke="#000" stroke-width="10" stroke-linejoin="round">
      <path d="M1185 10 L1205 30 L1060 175 L1105 220 L915 340 L985 160 L1035 200 Z"/>
    </g>
  </svg>
</main>
</body>
</html>
```